Roof Plumbing Company needs simple, modern business card using the attached logo and below details:

Glen Marwick
Kestrel Roofing Pty Ltd
ABN: 58 217 934 062
Phone: 0417 286 503
Email: kestrelroofing@mailvista.com
Website: kestrelroofing.com.au

For all of your metal roof plumbing requirements contact Kestrel Roofing for an obligation free quote - no job too big or to small!

Industry/Entity Type

Business

Contact Information for Business Card

Glen Marwick
Kestrel Roofing Pty Ltd
ABN 58 217 934 062
0417 286 503
kestrelroofing@mailvista.com
kestrelroofing.com.au

Requirements
Must have
• Bright eye catching design, professional look

```html
<!DOCTYPE html>
<html lang="en">
<head>
<meta charset="utf-8">
<title>Kestrel Roofing – Business Card</title>
<link href="https://fonts.googleapis.com/css2?family=Source+Sans+3:ital,wght@0,400;0,600;0,700;1,700&display=swap" rel="stylesheet">
<style>
  :root {
    --bg: #3a3a3a;
    --card-white: #f7f7f7;
    --brand-red: #b5120f;
    --red-deep: #8e0f0c;
    --red-bright: #d4150f;
    --text-dark: #444444;
    --text-mid: #555555;
    --rule: #d0d0d0;
    --white: #ffffff;
  }
  * { margin: 0; padding: 0; box-sizing: border-box; }
  html, body {
    width: 1200px; height: 750px; overflow: hidden;
    background: var(--bg);
    font-family: "Source Sans 3", sans-serif;
  }
  .stage { position: relative; width: 1200px; height: 750px; }
  .card {
    position: absolute; top: 228px;
    width: 461px; height: 262px;
    overflow: hidden;
  }
  /* Front */
  .card-front { left: 124px; background: var(--card-white); }
  .front-brand {
    position: absolute; left: 40px; top: 98px; width: 180px;
    display: flex; align-items: center; gap: 8px;
    color: var(--brand-red); font-weight: 700; font-size: 22px;
  }
  .brand-square { width: 12px; height: 12px; background: var(--brand-red); flex: none; }
  .divider {
    position: absolute; left: 234px; top: 60px; width: 1px; height: 124px;
    background: var(--rule);
  }
  .details { position: absolute; left: 259px; top: 60px; color: var(--text-dark); }
  .name { color: var(--brand-red); font-size: 18px; font-weight: 600; line-height: 22px; }
  .company { font-size: 11.5px; font-weight: 600; margin-top: 7px; line-height: 14px; }
  .abn { font-size: 11.5px; line-height: 14px; color: var(--text-mid); }
  .contact-list { list-style: none; margin-top: 10px; }
  .contact-list li {
    display: flex; align-items: center; gap: 6px;
    font-size: 11.5px; line-height: 17.5px; color: var(--text-mid);
  }
  .contact-list svg { width: 11px; height: 11px; flex: none; }
  .footer-rule {
    position: absolute; left: 0; right: 0; top: 239px; height: 2px; background: #8a8a8a;
  }
  .tagline-band {
    position: absolute; left: 0; right: 0; top: 242px; height: 20px;
    background: linear-gradient(var(--brand-red), var(--red-deep));
    color: var(--white); font-style: italic; font-weight: 700; font-size: 12.5px;
    text-align: center; line-height: 20px;
  }
  /* Back */
  .card-back {
    left: 618px;
    background: radial-gradient(ellipse at 50% 35%, var(--red-bright) 0%, #b1110d 45%, var(--red-deep) 100%);
  }
  .back-brand {
    position: absolute; left: 0; right: 0; top: 96px;
    display: flex; justify-content: center; align-items: center; gap: 8px;
    color: var(--white); font-weight: 700; font-size: 24px;
  }
  .back-brand .brand-square { background: var(--white); }
  .quote-button {
    position: absolute; left: 176px; top: 157px; width: 110px; height: 37px;
    background: var(--white); border-radius: 4px;
    text-align: center; color: var(--brand-red);
  }
  .quote-small { display: block; font-size: 11.5px; line-height: 13px; margin-top: 3px; }
  .quote-large { display: block; font-size: 17px; line-height: 19px; }
  .service-line {
    position: absolute; left: 0; right: 0; top: 196px;
    text-align: center; font-size: 11px; color: #7a0d0a;
  }
</style>
</head>
<body>
<main class="stage">
  <section class="card card-front">
    <div class="front-brand"><span class="brand-square"></span><span>Kestrel Roofing</span></div>
    <div class="divider"></div>
    <div class="details">
      <p class="name">Glen Marwick</p>
      <p class="company">Kestrel Roofing Pty Ltd</p>
      <p class="abn">ABN 58 217 934 062</p>
      <ul class="contact-list">
        <li>
          <svg viewBox="0 0 12 12"><path d="M2.5 1 L4.5 1 L5.3 3.3 L4 4.3 C4.7 5.8 6.2 7.3 7.7 8 L8.7 6.7 L11 7.5 L11 9.5 C11 10.4 10.3 11 9.5 11 C5 11 1 7 1 2.5 C1 1.7 1.6 1 2.5 1 Z" fill="#b5120f"/></svg>
          0417 286 503
        </li>
        <li>
          <svg viewBox="0 0 12 12"><rect x="0.5" y="2.5" width="11" height="7.5" fill="#b5120f"/><path d="M0.8 3 L6 7 L11.2 3" stroke="#fff" stroke-width="1" fill="none"/></svg>
          kestrelroofing@mailvista.com
        </li>
        <li>
          <svg viewBox="0 0 12 12"><circle cx="6" cy="6" r="5.5" fill="#b5120f"/><ellipse cx="6" cy="6" rx="2.3" ry="5.3" stroke="#fff" stroke-width="0.8" fill="none"/><line x1="0.8" y1="6" x2="11.2" y2="6" stroke="#fff" stroke-width="0.8"/></svg>
          www.kestrelroofing.com.au
        </li>
      </ul>
    </div>
    <div class="footer-rule"></div>
    <div class="tagline-band">No job too big or to small!</div>
  </section>

  <section class="card card-back">
    <div class="back-brand"><span class="brand-square"></span><span>Kestrel Roofing</span></div>
    <div class="quote-button">
      <span class="quote-small">Get your</span>
      <span class="quote-large">Free Quote</span>
    </div>
    <p class="service-line">Metal roof plumbing</p>
  </section>
</main>
</body>
</html>
```